" A Voltrana é uma empresa cuja especialidade é atuar diretamente no setor de energia, oferecendo a seus clientes gestão de energia e utilidades (água, gás, vapor, ar comprimido) com o objetivo principal de obter informações, padrões e variáveis de consumo e também eficiência energética para agir de forma assertiva no foco do desperdício e na otimização da utilização dos recursos em um parque industrial ou edifício. "

```html
<!DOCTYPE html>
<html lang="pt-BR">
<head>
<meta charset="UTF-8">
<title>Voltrana — Envelopes</title>
<link rel="stylesheet" href="https://fonts.googleapis.com/css2?family=Montserrat:wght@400;600;800&display=swap">
<style>
  :root {
    --backdrop: #ece8e3;
    --paper: #ffffff;
    --flap-yellow: #f8bb2a;
    --flap-grey: #e9e9e9;
    --brand-yellow: #f3a712;
    --brand-green: #2f8f3a;
    --ink: #4a4a4a;
    --shadow: rgba(0,0,0,0.18);
  }
  * { margin: 0; padding: 0; box-sizing: border-box; }
  html, body { width: 1200px; height: 1200px; overflow: hidden; }
  body {
    background: var(--backdrop);
    font-family: "Montserrat", sans-serif;
    position: relative;
  }
  .envelope {
    position: absolute;
    top: 190px;
    width: 520px;
    height: 850px;
  }
  .envelope--front { left: 78px; }
  .envelope--back { left: 620px; }
  .envelope__flap {
    position: absolute;
    top: 0; left: 0;
    width: 520px; height: 92px;
  }
  .envelope__body {
    position: absolute;
    top: 90px; left: 0;
    width: 520px; height: 760px;
    background: var(--paper);
    box-shadow: 0 6px 18px var(--shadow);
    overflow: hidden;
  }

  /* Large brand name on the front, lower left */
  .front-mark {
    position: absolute;
    left: 0;
    bottom: 120px;
    display: flex;
    align-items: center;
    gap: 16px;
  }
  .front-mark__dot {
    width: 40px; height: 40px;
    border-radius: 50%;
    background: var(--brand-green);
  }
  .front-mark__name {
    font-weight: 800;
    font-size: 64px;
    line-height: 1;
    letter-spacing: 1px;
    color: var(--brand-yellow);
    text-transform: uppercase;
  }

  /* Plain accent disc on the back, lower right */
  .back-accent {
    position: absolute;
    right: -60px;
    bottom: 40px;
    width: 170px; height: 170px;
    border-radius: 50%;
    background: var(--brand-yellow);
  }

  .sender {
    position: absolute;
    left: 30px;
    bottom: 28px;
    color: var(--ink);
  }
  .sender__brand {
    display: flex;
    align-items: center;
    gap: 8px;
  }
  .sender__dot {
    width: 14px; height: 14px;
    border-radius: 50%;
    background: var(--brand-green);
  }
  .sender__name {
    font-weight: 800;
    font-size: 26px;
    letter-spacing: 1px;
    color: var(--brand-yellow);
    text-transform: uppercase;
  }
  .sender__tagline {
    font-size: 9px;
    letter-spacing: 2.4px;
    color: var(--brand-green);
    margin: 2px 0 16px 22px;
    text-transform: uppercase;
  }
  .contact { list-style: none; }
  .contact__item {
    display: flex;
    align-items: center;
    gap: 8px;
    font-size: 9.5px;
    line-height: 1;
    margin-bottom: 9px;
  }
  .contact__icon { width: 12px; height: 12px; flex: none; }
</style>
</head>
<body>

  <section class="envelope envelope--front" aria-label="Envelope, frente">
    <svg class="envelope__flap" viewBox="0 0 520 92" aria-hidden="true">
      <path d="M0 92 L6 26 Q8 6 30 6 L490 6 Q512 6 514 26 L520 92 Z" fill="var(--flap-yellow)"/>
    </svg>
    <div class="envelope__body">
      <div class="front-mark">
        <span class="front-mark__dot"></span>
        <span class="front-mark__name">Voltrana</span>
      </div>
    </div>
  </section>

  <section class="envelope envelope--back" aria-label="Envelope, verso">
    <svg class="envelope__flap" viewBox="0 0 520 92" aria-hidden="true">
      <path d="M0 92 L6 26 Q8 6 30 6 L490 6 Q512 6 514 26 L520 92 Z" fill="var(--flap-grey)"/>
    </svg>
    <div class="envelope__body">
      <span class="back-accent" aria-hidden="true"></span>
      <div class="sender">
        <div class="sender__brand">
          <span class="sender__dot"></span>
          <span class="sender__name">Voltrana</span>
        </div>
        <p class="sender__tagline">gestão de energia</p>
        <ul class="contact">
          <li class="contact__item">
            <svg class="contact__icon" viewBox="0 0 12 12"><path d="M6 0.5a4 4 0 0 0-4 4c0 3 4 7 4 7s4-4 4-7a4 4 0 0 0-4-4z" fill="var(--brand-green)"/><circle cx="6" cy="4.5" r="1.4" fill="#fff"/></svg>
            Rua das Turbinas, 120 - Campinas - SP
          </li>
          <li class="contact__item">
            <svg class="contact__icon" viewBox="0 0 12 12"><rect width="12" height="12" rx="2" fill="var(--brand-green)"/><path d="M3.5 2.5l1.5 0 .6 2-1 .8a5 5 0 0 0 2.1 2.1l.8-1 2 .6 0 1.5c-3.5.4-6.4-2.5-6-6z" fill="#fff"/></svg>
            (19) 3000-4100 - (19) 98000-4100
          </li>
          <li class="contact__item">
            <svg class="contact__icon" viewBox="0 0 12 12"><rect width="12" height="12" rx="2" fill="var(--brand-green)"/><rect x="2.5" y="3.5" width="7" height="5" fill="none" stroke="#fff" stroke-width="0.9"/><path d="M2.5 3.5L6 6.3 9.5 3.5" fill="none" stroke="#fff" stroke-width="0.9"/></svg>
            contato@voltrana.com.br
          </li>
          <li class="contact__item">
            <svg class="contact__icon" viewBox="0 0 12 12"><circle cx="6" cy="6" r="6" fill="var(--brand-green)"/><circle cx="6" cy="6" r="3.6" fill="none" stroke="#fff" stroke-width="0.8"/><path d="M2.4 6h7.2M6 2.4c-1.8 2-1.8 5.2 0 7.2M6 2.4c1.8 2 1.8 5.2 0 7.2" fill="none" stroke="#fff" stroke-width="0.7"/></svg>
            www.voltrana.com.br
          </li>
        </ul>
      </div>
    </div>
  </section>

</body>
</html>
```